Bref créative
Quorel Stationary
Stationary and Business Cards
I need double sided standard sized Business Card [3.5" x 2"]
show me your ideas
Corporate
Marcus Toddin
Chief Executive Officer
Halvenor Business Tower
9th Floor
PO Box 58217
Marenta
Eldoria
mt@quorel.co
www.quorel.co
Show me your ideas

```html
<!DOCTYPE html>
<html lang="en">
<head>
<meta charset="utf-8">
<title>Quorel Stationary – Corporate Identity</title>
<link rel="stylesheet" href="https://fonts.googleapis.com/css2?family=Roboto:wght@400;700&display=swap">
<style>
  :root{
    --bg:#e6e9ec;
    --paper:#ffffff;
    --blue:#1c8fd9;
    --blue-light:#63bdf0;
    --blue-deep:#1570b8;
    --grey-line:#c8cdd2;
    --text:#4a4f55;
    --text-soft:#8a9097;
    --font:"Roboto", Arial, sans-serif;
  }
  *{box-sizing:border-box;margin:0;padding:0}
  html,body{width:1200px;height:799px;overflow:hidden}
  body{background:var(--bg);font-family:var(--font);color:var(--text);position:relative}

  .piece{position:absolute;background:var(--paper);overflow:hidden;box-shadow:0 2px 8px rgba(0,0,0,.12)}
  .band{position:absolute;left:0;bottom:0;width:100%}

  .brand-name{position:absolute;font-family:var(--font);font-weight:700;color:var(--blue-deep);line-height:1}

  /* Business card front */
  .card-front{left:50px;top:175px;width:320px;height:183px}
  .card-front .brand-name{left:18px;top:24px;font-size:20px}
  .card-front .holder{position:absolute;right:18px;top:22px;text-align:right}
  .holder-name{font-size:17px;font-weight:700;color:var(--blue);white-space:nowrap}
  .holder-title{font-size:9px;color:var(--text-soft);margin-top:2px}
  .card-front .band{height:80px}
  .card-front .contact{position:absolute;left:18px;bottom:12px;font-size:8px;line-height:1.45;color:#fff}

  /* Business card back */
  .card-back{left:50px;top:400px;width:320px;height:183px;background:var(--blue)}
  .card-back .band{height:183px}
  .card-back .brand-name{left:0;right:0;top:76px;text-align:center;font-size:26px;color:#fff}
  .card-back .web{position:absolute;left:0;right:0;bottom:16px;text-align:center;font-size:9px;letter-spacing:2px;color:#fff}

  /* Letterhead */
  .letterhead{left:410px;top:130px;width:380px;height:537px}
  .letterhead .brand-name{left:28px;top:32px;font-size:22px}
  .letter-body{position:absolute;left:28px;right:28px;top:96px;font-size:7.5px;line-height:1.55}
  .recipient{margin-bottom:12px}
  .salutation{margin-bottom:8px}
  .letter-body p{margin-bottom:8px;color:var(--text-soft)}
  .signature{width:70px;height:20px;margin-top:14px;background:#edf2f7;border-radius:3px}
  .letterhead .band{height:80px}
  .letterhead .contact{position:absolute;right:28px;bottom:12px;text-align:right;font-size:7.5px;line-height:1.45;color:#fff}

  /* Envelope */
  .envelope{left:830px;top:130px;width:330px;height:165px}
  .envelope .brand-name{left:22px;top:26px;font-size:17px}
  .envelope .band{height:60px}

  /* Compliment slips */
  .slip{left:830px;width:330px;height:150px}
  .slip-a{top:330px}
  .slip-b{top:510px}
  .slip .brand-name{left:20px;top:24px;font-size:16px}
  .slip .holder{position:absolute;left:20px;top:60px}
  .slip .holder-name{font-size:13px}
  .slip .holder-title{font-size:8px}
  .slip .band{height:44px}
  .slip .contact{position:absolute;right:18px;top:20px;text-align:right;font-size:7.5px;line-height:1.45;color:var(--text)}
</style>
</head>
<body>

<svg width="0" height="0" style="position:absolute" aria-hidden="true">
  <defs>
    <linearGradient id="band-fill" x1="0" y1="0" x2="1" y2="0">
      <stop offset="0" stop-color="#63bdf0"/>
      <stop offset="1" stop-color="#1c8fd9"/>
    </linearGradient>
  </defs>
</svg>

<!-- Business card front -->
<section class="piece card-front">
  <span class="brand-name">Quorel</span>
  <div class="holder">
    <div class="holder-name">Marcus Toddin</div>
    <div class="holder-title">Chief Executive Officer</div>
  </div>
  <svg class="band" viewBox="0 0 320 80" preserveAspectRatio="none" aria-hidden="true">
    <rect x="0" y="0" width="320" height="2" fill="#c8cdd2"/>
    <rect x="0" y="8" width="320" height="72" fill="url(#band-fill)"/>
  </svg>
  <div class="contact">
    Halvenor Business Tower, 9th Floor<br>
    PO Box 58217, Marenta, Eldoria<br>
    mt@quorel.co · www.quorel.co
  </div>
</section>

<!-- Business card back -->
<section class="piece card-back">
  <svg class="band" viewBox="0 0 320 183" preserveAspectRatio="none" aria-hidden="true">
    <rect x="0" y="0" width="320" height="40" fill="#ffffff"/>
    <rect x="0" y="46" width="320" height="2" fill="#c8cdd2"/>
    <rect x="0" y="140" width="320" height="43" fill="#1570b8"/>
  </svg>
  <span class="brand-name">Quorel</span>
  <div class="web">www.quorel.co</div>
</section>

<!-- Letterhead -->
<section class="piece letterhead">
  <span class="brand-name">Quorel</span>
  <div class="letter-body">
    <div class="recipient">Sample Some Body<br>12 Ardel St<br>Sydney, Australia</div>
    <div class="salutation">Dear Somebody,</div>
    <p>Lorem ipsum dolor sit amet, consectetuer adipiscing elit, sed diam nonummy nibh euismod tincidunt ut laoreet dolore magna aliquam erat volutpat. Ut wisi enim ad minim veniam, quis nostrud exerci tation ullamcorper suscipit lobortis nisl ut aliquip ex ea commodo consequat.</p>
    <p>Duis autem vel eum iriure dolor in hendrerit in vulputate velit esse molestie consequat, vel illum dolore eu feugiat nulla facilisis at vero eros et accumsan et iusto odio dignissim qui blandit praesent luptatum zzril delenit augue duis dolore.</p>
    <p>Lorem ipsum dolor sit amet, consectetuer adipiscing elit, sed diam nonummy nibh euismod tincidunt ut laoreet dolore magna aliquam erat volutpat. Duis autem vel eum iriure dolor in hendrerit in vulputate velit esse molestie consequat.</p>
    <div class="signature" role="img" aria-label="Handwritten signature"></div>
  </div>
  <svg class="band" viewBox="0 0 380 80" preserveAspectRatio="none" aria-hidden="true">
    <rect x="0" y="0" width="380" height="2" fill="#c8cdd2"/>
    <rect x="0" y="8" width="380" height="72" fill="url(#band-fill)"/>
  </svg>
  <div class="contact">
    Halvenor Business Tower, 9th Floor<br>
    PO Box 58217, Marenta, Eldoria<br>
    mt@quorel.co · www.quorel.co
  </div>
</section>

<!-- Envelope -->
<section class="piece envelope">
  <span class="brand-name">Quorel</span>
  <svg class="band" viewBox="0 0 330 60" preserveAspectRatio="none" aria-hidden="true">
    <rect x="0" y="0" width="330" height="2" fill="#c8cdd2"/>
    <rect x="0" y="8" width="330" height="52" fill="url(#band-fill)"/>
  </svg>
</section>

<!-- Compliment slips -->
<section class="piece slip slip-a">
  <span class="brand-name">Quorel</span>
  <div class="holder">
    <div class="holder-name">Marcus Toddin</div>
    <div class="holder-title">Chief Executive Officer</div>
  </div>
  <div class="contact">
    Halvenor Business Tower<br>9th Floor, PO Box 58217<br>Marenta, Eldoria<br>mt@quorel.co
  </div>
  <svg class="band" viewBox="0 0 330 44" preserveAspectRatio="none" aria-hidden="true">
    <rect x="0" y="0" width="330" height="2" fill="#c8cdd2"/>
    <rect x="0" y="8" width="330" height="36" fill="url(#band-fill)"/>
  </svg>
</section>

<section class="piece slip slip-b">
  <span class="brand-name">Quorel</span>
  <div class="holder">
    <div class="holder-name">Marcus Toddin</div>
    <div class="holder-title">Chief Executive Officer</div>
  </div>
  <div class="contact">
    Halvenor Business Tower<br>9th Floor, PO Box 58217<br>Marenta, Eldoria<br>www.quorel.co
  </div>
  <svg class="band" viewBox="0 0 330 44" preserveAspectRatio="none" aria-hidden="true">
    <rect x="0" y="0" width="330" height="2" fill="#c8cdd2"/>
    <rect x="0" y="8" width="330" height="36" fill="url(#band-fill)"/>
  </svg>
</section>

</body>
</html>
```